Redo a PPT pres. - Real Estate in Brazil - Socially equitable investments in Social Housing

We need to redo the presentation attached. It is an institutional presentation to attract local and foreign investors to invest in Brazilian Social Housing Projects structured by our company "RTV".
A middle class of 100 million, a housing deficit of 9M, a strong political will & positive income generation trends constitute grounds for a significant demand in social housing.
This make a perfect scheme for investors to invest in Brazilian Social Housing.
"RTV", is a consulting "boutique" focused in Brazilian real estate, specialized in structuring, analyzing and originating Brazilian social housing projects.
RTV is part of the group RTP. RTP is structured to create value through each step of the residential real estate business - structuring, financing, sales, marketing and technology.
We would like to see designs that use mainly the color blue. The final design should communicate financial safety and professionalism. In order to reach our needs, the designer will need to have basic understanding of finance and investment in order to highlight the most important information.
The idea is to receive back the PPT with each page redesigned and an homogeneous identity.
To all designers,
Target Market(s)
Institutional Investors and wealthy individuals
Industry/Entity Type
Residential
Look and feel
Each slider illustrates characteristics of the customer's brand and the style your logo design should communicate.

```html
<!DOCTYPE html>
<html lang="en">
<head>
<meta charset="utf-8">
<title>Social Housing in Brazil – RTV</title>
<link href="https://fonts.googleapis.com/css2?family=PT+Sans:wght@400;700&display=swap" rel="stylesheet">
<style>
  :root {
    --blue: #2a72bb;
    --blue-light: #5b9bd5;
    --blue-pale: #8ab8e6;
    --navy: #0f2c52;
    --navy-mid: #1b4272;
    --ink: #555d66;
    --page: #ffffff;
  }
  * { margin: 0; padding: 0; box-sizing: border-box; }
  html, body { width: 1200px; height: 329px; overflow: hidden; background: var(--page); }
  body { position: relative; font-family: "PT Sans", sans-serif; }

  .slide {
    position: absolute; top: 47px; width: 330px; height: 248px;
    background: #fff; box-shadow: 2px 3px 6px rgba(0,0,0,.35); overflow: hidden;
  }
  .slide--cover { left: 34px; }
  .slide--how { left: 434px; }
  .slide--time { left: 820px; }

  .brand { position: absolute; font-weight: 700; color: var(--navy); letter-spacing: .5px; }
  .slide--cover .brand { left: 10px; top: 23px; font-size: 13px; }
  .footer-brand { left: 12px; bottom: 6px; font-size: 9px; }
  .page-no { position: absolute; right: 10px; bottom: 7px; font-size: 6px; color: var(--ink); }

  .skyline-art {
    position: absolute; left: 0; top: 44px; width: 330px; height: 114px;
    background: linear-gradient(180deg, #ffffff 0%, #6f9fd6 40%, #1d3f73 100%);
  }
  .cover-band {
    position: absolute; left: 0; top: 158px; width: 100%; height: 82px;
    background: var(--blue); color: #fff; padding: 23px 0 0 26px;
  }
  .cover-band h1 { font-size: 14px; font-weight: 700; letter-spacing: .3px; }
  .cover-band p { font-size: 9.5px; font-weight: 700; margin-top: 12px; letter-spacing: .4px; }
  .cover-rule { position: absolute; left: 0; bottom: 0; width: 100%; height: 8px; background: var(--navy); }

  .slide-header {
    position: absolute; left: 0; top: 0; width: 100%; height: 44px;
    background: var(--blue); color: #fff; padding: 9px 0 0 12px;
  }
  .slide-header h2 { font-size: 14.5px; font-weight: 400; line-height: 1.1; }
  .slide--time .slide-header h2 { padding-top: 7px; }
  .header-skyline {
    position: absolute; right: 14px; top: 12px; width: 70px; height: 20px;
    background: linear-gradient(180deg, #bcd7f2, #eaf3fc);
  }
  .subtitle { position: absolute; left: 12px; top: 52px; font-size: 11px; font-weight: 700; color: var(--blue); }

  .donut { position: absolute; left: 0; top: 0; }
  .donut text { font-family: "PT Sans", sans-serif; font-size: 5.4px; fill: #fff; text-anchor: middle; }

  .agenda { position: absolute; left: 18px; top: 54px; list-style: none; font-size: 9.5px; }
  .agenda li { color: var(--ink); margin-bottom: 7.5px; line-height: 1.25; }
  .agenda .topic { color: var(--blue); }
  .agenda .num { display: inline-block; width: 14px; color: var(--blue); }
  .agenda .sub { display: block; padding-left: 14px; }

  .clock-art {
    position: absolute; left: 256px; top: 110px; width: 48px; height: 56px;
    background: radial-gradient(circle at 50% 55%, #ffffff 35%, var(--blue) 37%);
    border-radius: 50%;
  }
</style>
</head>
<body>

  <section class="slide slide--cover">
    <div class="brand">RTV</div>
    <div class="skyline-art" role="img" aria-label="City skyline illustration in shades of blue"></div>
    <div class="cover-band">
      <h1>SOCIAL HOUSING IN BRAZIL</h1>
      <p>HIGH YIELD RETURN FOR A QUASI SOVEREIGN RISK</p>
    </div>
    <div class="cover-rule"></div>
  </section>

  <section class="slide slide--how">
    <header class="slide-header">
      <h2>How to invest in social housing in<br>Brazil?</h2>
      <div class="header-skyline" role="img" aria-label="Small city skyline illustration"></div>
    </header>
    <p class="subtitle">A socially conscious &amp; lucrative investment</p>
    <svg class="donut" width="330" height="248" viewBox="0 0 330 248" aria-label="Investment model wheel">
      <g stroke="#fff" stroke-width="1">
        <path fill="#0f2c52" d="M165 79 A78 78 0 0 1 220.2 101.8 L193.3 128.7 A40 40 0 0 0 165 117 Z"/>
        <path fill="#143560" d="M220.2 101.8 A78 78 0 0 1 243 157 L205 157 A40 40 0 0 0 193.3 128.7 Z"/>
        <path fill="#1b4272" d="M243 157 A78 78 0 0 1 220.2 212.2 L193.3 185.3 A40 40 0 0 0 205 157 Z"/>
        <path fill="#214f88" d="M220.2 212.2 A78 78 0 0 1 165 235 L165 197 A40 40 0 0 0 193.3 185.3 Z"/>
        <path fill="#2a66a8" d="M165 235 A78 78 0 0 1 109.8 212.2 L136.7 185.3 A40 40 0 0 0 165 197 Z"/>
        <path fill="#3577bd" d="M109.8 212.2 A78 78 0 0 1 87 157 L125 157 A40 40 0 0 0 136.7 185.3 Z"/>
        <path fill="#4b8acb" d="M87 157 A78 78 0 0 1 109.8 101.8 L136.7 128.7 A40 40 0 0 0 125 157 Z"/>
        <path fill="#8ab8e6" d="M109.8 101.8 A78 78 0 0 1 165 79 L165 117 A40 40 0 0 0 136.7 128.7 Z"/>
      </g>
      <text x="188" y="92"><tspan x="188">Building</tspan><tspan x="188" dy="6">housing units</tspan><tspan x="188" dy="6">for low to</tspan><tspan x="188" dy="6">middle class</tspan><tspan x="188" dy="6">buyers</tspan></text>
      <text x="222" y="129"><tspan x="222">Investing in</tspan><tspan x="222" dy="6">individual</tspan><tspan x="222" dy="6">projects</tspan></text>
      <text x="222" y="171"><tspan x="222">Management</tspan><tspan x="222" dy="6">Specialized</tspan><tspan x="222" dy="6">international</tspan><tspan x="222" dy="6">&amp; local team</tspan></text>
      <text x="190" y="207"><tspan x="190">Co-investing</tspan><tspan x="190" dy="6">with local /</tspan><tspan x="190" dy="6">mid-size</tspan><tspan x="190" dy="6">developers</tspan></text>
      <text x="142" y="205"><tspan x="142">Co-financed</tspan><tspan x="142" dy="6">by</tspan><tspan x="142" dy="6">government</tspan></text>
      <text x="108" y="170"><tspan x="108">Equity</tspan><tspan x="108" dy="6">participation</tspan><tspan x="108" dy="6">of R$2-10</tspan><tspan x="108" dy="6">millions</tspan></text>
      <text x="108" y="132"><tspan x="108">Time Horizon</tspan><tspan x="108" dy="6">3-4 years</tspan></text>
      <text x="142" y="100"><tspan x="142">Target IRR</tspan><tspan x="142" dy="6">25-30%</tspan></text>
    </svg>
    <div class="brand footer-brand">RTV</div>
    <span class="page-no">2</span>
  </section>

  <section class="slide slide--time">
    <header class="slide-header">
      <h2>The time is now!</h2>
      <div class="header-skyline" role="img" aria-label="Small city skyline illustration"></div>
    </header>
    <ol class="agenda">
      <li><span class="num">1.</span><span class="topic">Macro-environment &amp; Mortgage market:</span> Green Light</li>
      <li><span class="num">2.</span><span class="topic">A sophisticated &amp; successful program:</span> Catalyst</li>
      <li><span class="num">3.</span><span class="topic">Investment Structure of a typical project:</span><span class="sub">Leverage &amp; Limited Risks</span></li>
      <li><span class="num">4.</span><span class="topic">Small &amp; mid size developers:</span><span class="sub">A partner by choice</span></li>
      <li><span class="num">5.</span><span class="topic">RTV:</span> Value added &amp; Risk mitigation</li>
      <li><span class="num">6.</span><span class="topic">RTP:</span> RTV, part of an integrated family of companies</li>
      <li><span class="num">7.</span><span class="topic">Appendix:</span> Next step…RTV Fund (2013)</li>
    </ol>
    <div class="clock-art" role="img" aria-label="Blue alarm clock illustration"></div>
    <div class="brand footer-brand">RTV</div>
    <span class="page-no">3</span>
  </section>

</body>
</html>
```